Update our business cards to match our awesome new website

Need a new design for company business cards. We have recently revamped our website and would like our business cards to get a refresh too. I've uploaded the company artwork, logo, as well as the Branding Deck to better understand the look & feel of our brand. Please visit the website at bellcrestholdingsoh.com.

Industry/Entity Type

Real Estate

Contact Information for Business Card

must use the colors outlined in the Branding Deck uploaded to the site, or the colors of our logo.

Font styles to use
Other font styles liked:
• Calibri

Requirements
Must have
• Required items: Name, title, company logo, address: 217 Fennimore Ave. Suite 300, Lakeport, OH 44093, email address: glen@bellcrestholdingsOH.com, company phone 800-555-0172, cell: 216-555-0148
Nice to have
• a more simple design. not complicated
Should not have
• cartoonish characters, or whimsical writing or artwork, stay within our branding colors

```html
<!DOCTYPE html>
<html lang="en">
<head>
<meta charset="utf-8">
<title>Bellcrest Holdings – Business Card</title>
<link rel="stylesheet" href="https://fonts.googleapis.com/css2?family=Open+Sans:wght@400;600;700&display=swap">
<style>
  :root {
    --page: #ececec;
    --card: #ffffff;
    --brand-green: #6cb33f;
    --ink: #1e1e1e;
    --ink-soft: #444444;
    --shadow: rgba(0, 0, 0, 0.12);
  }
  * { box-sizing: border-box; margin: 0; padding: 0; }
  html, body {
    width: 1200px;
    height: 900px;
    overflow: hidden;
    background: var(--page);
    font-family: "Open Sans", "Calibri", sans-serif;
    color: var(--ink);
  }
  .canvas { position: relative; width: 1200px; height: 900px; }

  .card {
    position: absolute;
    width: 560px;
    height: 320px;
    background: var(--card);
    box-shadow: 0 6px 18px var(--shadow);
  }
  .card--front { left: 80px; top: 90px; }
  .card--back { left: 560px; top: 490px; }

  /* Wordmark */
  .wordmark {
    display: flex;
    align-items: center;
    gap: 14px;
  }
  .wordmark__dot {
    border-radius: 50%;
    background: var(--brand-green);
    flex: none;
  }
  .wordmark__name {
    font-weight: 600;
    text-transform: uppercase;
    letter-spacing: 0.06em;
    color: var(--ink);
    line-height: 1.1;
  }
  .card--front .wordmark {
    position: absolute;
    left: 0; right: 0; top: 0; bottom: 0;
    justify-content: center;
  }
  .card--front .wordmark__dot { width: 36px; height: 36px; }
  .card--front .wordmark__name { font-size: 30px; }

  .card--back .wordmark {
    position: absolute;
    right: 30px;
    top: 38px;
    gap: 8px;
  }
  .card--back .wordmark__dot { width: 16px; height: 16px; }
  .card--back .wordmark__name { font-size: 15px; }

  /* Back content */
  .identity {
    position: absolute;
    left: 0;
    top: 128px;
    padding-left: 38px;
    border-left: 10px solid var(--brand-green);
  }
  .identity__name {
    font-size: 28px;
    font-weight: 700;
    color: var(--brand-green);
    text-transform: uppercase;
    letter-spacing: 0.01em;
    line-height: 1.05;
  }
  .identity__title {
    font-size: 19px;
    color: var(--ink-soft);
    line-height: 1.2;
  }

  .address {
    position: absolute;
    left: 48px;
    top: 208px;
    font-style: normal;
    font-size: 13.5px;
    color: var(--ink-soft);
    line-height: 1.35;
  }

  .contacts {
    position: absolute;
    left: 48px;
    top: 254px;
    list-style: none;
    font-size: 12.5px;
    color: var(--ink-soft);
    line-height: 1.3;
  }
  .contacts li { display: flex; align-items: center; gap: 6px; }
  .contacts svg { width: 11px; height: 11px; flex: none; fill: var(--brand-green); }
  .contacts .accent { color: var(--brand-green); }
</style>
</head>
<body>
<main class="canvas">

  <section class="card card--front" aria-label="Business card front">
    <div class="wordmark">
      <span class="wordmark__dot"></span>
      <span class="wordmark__name">Bellcrest Holdings of Ohio, LLC</span>
    </div>
  </section>

  <section class="card card--back" aria-label="Business card back">
    <div class="wordmark">
      <span class="wordmark__dot"></span>
      <span class="wordmark__name">Bellcrest Holdings of Ohio, LLC</span>
    </div>

    <div class="identity">
      <h1 class="identity__name">Glen Porter</h1>
      <p class="identity__title">Owner</p>
    </div>

    <address class="address">
      217 Fennimore Ave. Suite 300<br>
      Lakeport, OH 44093
    </address>

    <ul class="contacts">
      <li>
        <svg viewBox="0 0 12 12" aria-hidden="true"><path d="M2.5 1l2 2.2-1 1.3c.7 1.5 1.8 2.6 3.3 3.3l1.3-1 2.2 2-1 1.7C5.2 10.2 1.8 6.8 1 2.2z"/></svg>
        800-555-0172
      </li>
      <li>
        <svg viewBox="0 0 12 12" aria-hidden="true"><rect x="3" y="0.5" width="6" height="11" rx="1.2"/><rect x="4" y="2" width="4" height="6.5" fill="#fff"/></svg>
        216-555-0148
      </li>
      <li>
        <svg viewBox="0 0 12 12" aria-hidden="true"><rect x="0.5" y="2" width="11" height="8" rx="0.8"/><path d="M1 2.6l5 4 5-4" stroke="#fff" stroke-width="1.1" fill="none"/></svg>
        glen@bellcrestholdingsOH.com
      </li>
      <li>
        <svg viewBox="0 0 12 12" aria-hidden="true"><circle cx="6" cy="6" r="5.5"/><path d="M.8 6h10.4M6 .6c-2.6 3-2.6 7.8 0 10.8M6 .6c2.6 3 2.6 7.8 0 10.8" stroke="#fff" stroke-width="0.9" fill="none"/></svg>
        <span>www.<span class="accent">bellcrestholdingsoh</span>.com</span>
      </li>
    </ul>
  </section>

</main>
</body>
</html>
```